Managed Service Provider need new business cards

We are a small Maanged Service Provider of IT Services and need a new fresh design for our business cards. We want something impossible, fun and professional :)
Our services has a large range, but we are always fun and make sure our customers both get their issue sorted and also feel like they are "catching up with an old friend".
All our cards in the past has always been all black, with red and we need something fresher.
The back of card, we would like just a small list of what we do i think, but if someone has a better idea, please do something cool with the back of the card:
Managed IT Services
Productivity Solutions
Data Backup and Recovery
IT System Maintenance
Managed IT Security
More details can be found on our website tqnetworks.com.au
Industry/Entity Type
It Company
Contact Information for Business Card
Name: Dwayne Falstrup
Title: Director
Phone: 03 6193 4827
Mobile: 0412 587 239
Email: dwayne@tqnetworks.com.au
Web: www.tqnetworks.com.au

```html
<!DOCTYPE html>
<html lang="en">
<head>
<meta charset="utf-8">
<title>TQ Networks — Business Card</title>
<link rel="stylesheet" href="https://fonts.googleapis.com/css2?family=Open+Sans:wght@400;600;700&display=swap">
<style>
  :root {
    --stage: #d9d9db;
    --card-base: #1d1b1c;
    --card-panel: #262425;
    --panel-edge: #121011;
    --brand-red: #c4161c;
    --band-red: #b8141a;
    --text-light: #ffffff;
    --text-muted: #d6d6d6;
  }
  * { box-sizing: border-box; margin: 0; padding: 0; }
  html, body {
    width: 1200px; height: 900px; overflow: hidden;
    background: var(--stage);
    font-family: "Open Sans", Arial, sans-serif;
  }
  .sheet {
    position: relative; width: 1200px; height: 900px;
    display: flex; flex-direction: column; align-items: center;
    gap: 30px; padding-top: 35px;
  }
  .card {
    position: relative; width: 700px; height: 400px;
    background: var(--card-base);
    overflow: hidden;
    box-shadow: 0 6px 18px rgba(0,0,0,0.25);
  }
  .card-shapes { position: absolute; inset: 0; }

  .brand {
    position: absolute; display: flex; align-items: center; gap: 12px;
    color: var(--brand-red); font-weight: 700; font-size: 36px;
    letter-spacing: 1px; white-space: nowrap;
  }
  .brand-dot {
    width: 22px; height: 22px; border-radius: 50%;
    background: var(--brand-red);
  }
  .card-front .brand { left: 60px; top: 176px; }
  .card-back .brand { left: 60px; top: 176px; }

  .holder {
    position: absolute; right: 40px; top: 34px; text-align: right;
    color: var(--text-light);
  }
  .holder-name { font-size: 24px; letter-spacing: 1.5px; font-weight: 400; }
  .holder-name strong { font-weight: 700; }
  .holder-title { font-size: 16px; color: var(--text-muted); margin-top: 2px; }

  .contact-line {
    position: absolute; display: flex; align-items: center; gap: 12px;
    color: var(--text-light); font-size: 17px; height: 40px;
  }
  .contact-icon { width: 22px; height: 22px; flex: none; }
  .contact-phone { left: 428px; top: 200px; }
  .contact-web   { left: 423px; top: 252px; }
  .contact-mail  { left: 418px; top: 304px; }

  .services { position: absolute; inset: 0; list-style: none; }
  .service {
    position: absolute; background: var(--band-red);
    color: var(--text-light); font-size: 15px; font-weight: 600;
    line-height: 20px; padding: 4px 11px; border-radius: 4px; white-space: nowrap;
  }
  .service-1 { left: 446px; top: 62px; }
  .service-2 { left: 454px; top: 116px; }
  .service-3 { left: 462px; top: 170px; }
  .service-4 { left: 470px; top: 224px; }
  .service-5 { left: 478px; top: 278px; }
</style>
</head>
<body>
<main class="sheet">

  <section class="card card-front" aria-label="Business card front">
    <svg class="card-shapes" width="700" height="400" viewBox="0 0 700 400" aria-hidden="true">
      <polygon points="411,200 700,200 700,240 407,240" fill="var(--band-red)"/>
      <polygon points="406,252 700,252 700,292 402,292" fill="var(--band-red)"/>
      <polygon points="400,304 700,304 700,344 396,344" fill="var(--band-red)"/>
      <polygon points="0,0 346,0 424,120 394,400 0,400" fill="var(--panel-edge)"/>
      <polygon points="0,0 340,0 420,120 390,400 0,400" fill="var(--card-panel)"/>
    </svg>

    <div class="brand"><span class="brand-name">TQ NETWORKS</span><span class="brand-dot"></span></div>

    <div class="holder">
      <p class="holder-name">DWAYNE <strong>FALSTRUP</strong></p>
      <p class="holder-title">Director</p>
    </div>

    <p class="contact-line contact-phone">
      <svg class="contact-icon" viewBox="0 0 22 22" aria-hidden="true">
        <circle cx="11" cy="11" r="11" fill="#fff"/>
        <path d="M7 6.5c.6-.6 1.3-.5 1.7.1l1 1.5c.3.5.2 1-.2 1.4l-.6.5c.6 1.3 1.6 2.3 2.9 2.9l.5-.6c.4-.4.9-.5 1.4-.2l1.5 1c.6.4.7 1.1.1 1.7-1.2 1.2-3 1.1-5.3-1.2S5.8 7.7 7 6.5z" fill="var(--band-red)"/>
      </svg>
      <span>03 6193 4827, 0412 587 239</span>
    </p>
    <p class="contact-line contact-web">
      <svg class="contact-icon" viewBox="0 0 22 22" aria-hidden="true">
        <circle cx="11" cy="11" r="11" fill="#fff"/>
        <circle cx="11" cy="11" r="6.5" fill="none" stroke="var(--band-red)" stroke-width="1.4"/>
        <ellipse cx="11" cy="11" rx="2.8" ry="6.5" fill="none" stroke="var(--band-red)" stroke-width="1.2"/>
        <line x1="4.5" y1="11" x2="17.5" y2="11" stroke="var(--band-red)" stroke-width="1.2"/>
      </svg>
      <span>www.tqnetworks.com.au</span>
    </p>
    <p class="contact-line contact-mail">
      <svg class="contact-icon" viewBox="0 0 22 22" aria-hidden="true">
        <circle cx="11" cy="11" r="11" fill="#fff"/>
        <rect x="5.5" y="7" width="11" height="8" rx="1" fill="none" stroke="var(--band-red)" stroke-width="1.4"/>
        <polyline points="5.8,7.5 11,11.6 16.2,7.5" fill="none" stroke="var(--band-red)" stroke-width="1.3"/>
      </svg>
      <span>dwayne@tqnetworks.com.au</span>
    </p>
  </section>

  <section class="card card-back" aria-label="Business card back">
    <svg class="card-shapes" width="700" height="400" viewBox="0 0 700 400" aria-hidden="true">
      <polygon points="392,0 420,0 482,400 454,400" fill="var(--band-red)"/>
    </svg>

    <div class="brand"><span class="brand-name">TQ NETWORKS</span><span class="brand-dot"></span></div>

    <ul class="services">
      <li class="service service-1">Managed IT Services</li>
      <li class="service service-2">Productivity Solutions</li>
      <li class="service service-3">Data Backup and Recovery</li>
      <li class="service service-4">IT System Maintenance</li>
      <li class="service service-5">Managed IT Security</li>
    </ul>
  </section>

</main>
</body>
</html>
```